Kiosk Coin Venture: Safe and Secure Cash Money

Front of card: LOGO

Back of card:
$$$ FREE ATM PLACEMENT $$$
BENIFITS OF HAVING AN ATM AT YOUR BUSINESS
FREE ATM and BTM (Bitcoin) installation, maintenance, and loading.
Lower card processing fees
Stimulate more traffic.
Ease of access for customers
Maintain customers inside location.
Higher tips and spending

Contact me for more information!
Name: Tobias Merlano
Phone: (512) 638-9071 - Call or Text
Email: Tobias@KioskCoin.example

Contact Information for Business Card

The card should be shape of the logo. Only the back will have all the contact and business details.

Requirements
Must have
• The logo itself will be one side, the card will be the shape of the logo. contact details on back side.

```html
<!DOCTYPE html>
<html lang="en">
<head>
<meta charset="utf-8">
<title>Kiosk Coin Venture – Shield Business Card</title>
<link rel="stylesheet" href="https://fonts.googleapis.com/css2?family=Poppins:wght@400;600;700&display=swap">
<style>
  :root {
    --backdrop: #858585;
    --card-black: #1b1b1b;
    --card-deep: #121212;
    --silver-light: #f2f2f2;
    --silver-mid: #bdbdbd;
    --silver-dark: #7a7a7a;
    --text-white: #ffffff;
    --text-ink: #1a1a1a;
    --frame-line: #8c8c8c;
  }
  * { margin: 0; padding: 0; box-sizing: border-box; }
  html, body { width: 1200px; height: 834px; overflow: hidden; }
  body {
    background: var(--backdrop);
    font-family: "Poppins", Arial, sans-serif;
    position: relative;
  }
  .card-shapes { position: absolute; inset: 0; }
  .layer { position: absolute; inset: 0; }

  /* front */
  .front-brand {
    position: absolute;
    left: 141px; width: 436px; top: 330px;
    text-align: center;
    color: var(--silver-mid);
    font-weight: 700;
    font-size: 50px;
    line-height: 58px;
    letter-spacing: 1px;
    text-transform: uppercase;
  }

  /* back */
  .placement-banner {
    position: absolute;
    left: 644px; top: 157px; width: 384px; height: 33px;
    background: linear-gradient(90deg, var(--silver-dark), var(--silver-light) 45%, var(--silver-mid) 75%, var(--silver-dark));
    color: var(--text-ink);
    font-weight: 700; font-size: 20px;
    display: flex; align-items: center; justify-content: center;
    letter-spacing: 0.3px;
  }
  .benefits-title {
    position: absolute;
    left: 636px; width: 400px; top: 204px;
    text-align: center;
    color: var(--text-white);
    font-weight: 700; font-size: 20px; line-height: 23px;
  }
  .benefits-list {
    position: absolute;
    list-style: none;
    color: var(--text-white);
    font-size: 12.6px; line-height: 15.3px;
  }
  .benefits-list li { position: relative; padding-left: 18px; margin-bottom: 8px; }
  .benefits-list li::before {
    content: "✓";
    position: absolute; left: 0; top: 2px;
    width: 11px; height: 11px; border-radius: 50%;
    background: var(--silver-dark);
    color: var(--card-black);
    font-size: 8px; line-height: 11px; text-align: center; font-weight: 700;
  }
  .benefits-list.col-left { left: 652px; top: 274px; width: 175px; }
  .benefits-list.col-right { left: 851px; top: 274px; width: 170px; }

  .contact-name {
    position: absolute;
    left: 615px; width: 444px; top: 466px;
    text-align: center;
    font-weight: 700; font-size: 34px; letter-spacing: 1.5px;
    text-transform: uppercase;
    background: linear-gradient(90deg, var(--silver-dark), var(--silver-light) 40%, var(--silver-mid) 70%, var(--silver-light));
    -webkit-background-clip: text; background-clip: text;
    color: transparent;
  }
  .contact-or {
    position: absolute; left: 827px; top: 534px;
    color: var(--text-white); font-size: 9px; font-weight: 600;
  }
  .contact-phone, .contact-email {
    position: absolute; left: 615px; width: 444px;
    text-align: center; color: var(--text-white);
    font-size: 19.5px; font-weight: 400; letter-spacing: 0.3px;
  }
  .contact-phone { top: 561px; }
  .contact-email { top: 624px; font-size: 18.5px; }
</style>
</head>
<body>
  <svg class="card-shapes" width="1200" height="834" viewBox="0 0 1200 834" aria-hidden="true">
    <defs>
      <linearGradient id="silver-rim" x1="0" y1="0" x2="1" y2="1">
        <stop offset="0" stop-color="#e6e6e6"/>
        <stop offset="0.5" stop-color="#8a8a8a"/>
        <stop offset="1" stop-color="#f0f0f0"/>
      </linearGradient>
      <linearGradient id="card-fill" x1="0" y1="0" x2="0" y2="1">
        <stop offset="0" stop-color="#222"/>
        <stop offset="1" stop-color="#111"/>
      </linearGradient>
      <filter id="card-shadow" x="-10%" y="-10%" width="120%" height="120%">
        <feDropShadow dx="0" dy="3" stdDeviation="4" flood-opacity="0.35"/>
      </filter>
    </defs>

    <!-- front card -->
    <path class="card-front" filter="url(#card-shadow)" fill="url(#card-fill)" stroke="url(#silver-rim)" stroke-width="5"
          d="M359,75 L576,144 L576,600 Q576,640 540,660 L359,738 L178,660 Q141,640 141,600 L141,144 Z"/>
    <path class="card-front-inner" fill="none" stroke="url(#silver-rim)" stroke-width="2"
          d="M359,98 L556,160 L556,592 Q556,626 526,643 L359,714 L192,643 Q161,626 161,592 L161,160 Z"/>
    <circle class="brand-dot" cx="359" cy="250" r="36" fill="#bdbdbd"/>

    <!-- back card -->
    <path class="card-back" filter="url(#card-shadow)" fill="url(#card-fill)" stroke="url(#silver-rim)" stroke-width="5"
          d="M837,75 L1059,143 L1059,590 Q1059,640 1010,665 L837,753 L664,665 Q615,640 615,590 L615,143 Z"/>

    <!-- benefits frame with break for title -->
    <path class="benefits-frame" fill="none" stroke="#8c8c8c" stroke-width="1.2"
          d="M700,225 L636,225 L636,419 L1036,419 L1036,225 L975,225"/>

    <!-- divider under name -->
    <line class="name-divider" x1="717" y1="519" x2="954" y2="519" stroke="#7a7a7a" stroke-width="1"/>

    <!-- phone icon -->
    <g class="icon-phone">
      <circle cx="811" cy="542" r="11" fill="#9a9a9a"/>
      <path d="M806,536 q-1,6 4,11 q5,5 8,3 l1,-2 l-3,-2 l-2,1 q-3,-2 -5,-5 l1,-2 l-2,-3 Z" fill="#1b1b1b"/>
    </g>
    <!-- chat icon -->
    <g class="icon-chat">
      <circle cx="857" cy="542" r="11" fill="#9a9a9a"/>
      <path d="M851,537 h12 v8 h-8 l-3,3 v-3 h-1 Z" fill="#1b1b1b"/>
      <circle cx="854" cy="541" r="0.9" fill="#9a9a9a"/>
      <circle cx="857" cy="541" r="0.9" fill="#9a9a9a"/>
      <circle cx="860" cy="541" r="0.9" fill="#9a9a9a"/>
    </g>
    <!-- mail icon -->
    <g class="icon-mail">
      <circle cx="836" cy="609" r="11" fill="#9a9a9a"/>
      <rect x="829" y="604" width="14" height="10" fill="none" stroke="#1b1b1b" stroke-width="1.4"/>
      <path d="M829,604 L836,610 L843,604" fill="none" stroke="#1b1b1b" stroke-width="1.4"/>
    </g>
  </svg>

  <div class="layer card-front-content">
    <div class="front-brand">Kiosk<br>Coin<br>Venture</div>
  </div>

  <div class="layer card-back-content">
    <div class="placement-banner">$$$ FREE ATM PLACEMENT $$$</div>
    <h2 class="benefits-title">BENIFITS OF HAVING<br>AN ATM AT YOUR BUSINESS</h2>
    <ul class="benefits-list col-left">
      <li>FREE ATM and BTM (Bitcoin) installation, maintenance, and loading.</li>
      <li>Lower card processing fees</li>
      <li>Stimulate more traffic.</li>
    </ul>
    <ul class="benefits-list col-right">
      <li>Ease of access for customers</li>
      <li>Maintain customers inside location.</li>
      <li>Higher tips and spending</li>
    </ul>
    <div class="contact-name">Tobias Merlano</div>
    <div class="contact-or">or</div>
    <div class="contact-phone">(512) 638-9071</div>
    <div class="contact-email">Tobias@KioskCoin.example</div>
  </div>
</body>
</html>
```